MORVEK IT Limited Buisness card logo

I am setting up a IT Consultancy company and want a logo that is related to the IT industry, but also i am thinking that the A in MOR and the A in VEK are linked together maybe horizontally and vertically, also thought about the A being @ as it symbolises IT services. This logo will be used on paperwork, business cards and website.

Industry/Entity Type

Business

Contact Information for Business Card

Gareth Wilmslow
MORVEK IT Limited
IT Consultant
Mobile: 07912563084
Email: garethwk@fernmail.co.uk

Requirements
Must have
• IT Theme

```html
<!DOCTYPE html>
<html lang="en">
<head>
<meta charset="utf-8">
<title>MORVEK IT Limited – Business Card</title>
<link rel="stylesheet" href="https://fonts.googleapis.com/css2?family=Audiowide&family=Cinzel:wght@400&family=Marcellus&display=swap">
<style>
  :root {
    --ink: #000000;
    --paper: #ffffff;
    --olive: #677f00;
    --olive-deep: #4a5c0a;
    --silver: #c3c4c6;
    --silver-deep: #8e8f92;
    --teal: #03679a;
    --teal-deep: #024a6e;
    --brand-blue: #3a7abf;
    --band-blue: #3878bc;
    --title-green: #5c7a1e;
  }
  html, body {
    margin: 0;
    padding: 0;
    overflow: hidden;
    background: var(--paper);
  }
  .card {
    position: relative;
    width: 1200px;
    height: 688px;
    background: var(--ink);
    overflow: hidden;
  }
  .tone-panel {
    position: absolute;
    top: 0;
    height: 300px;
  }
  .tone-panel--olive  { left: 0;     width: 399px; background: linear-gradient(to bottom, var(--olive) 0%, var(--ink) 100%); }
  .tone-panel--silver { left: 399px; width: 398px; background: linear-gradient(to bottom, var(--silver) 0%, #1a1a1a 100%); }
  .tone-panel--teal   { left: 797px; width: 403px; background: linear-gradient(to bottom, var(--teal) 0%, var(--ink) 100%); }
  .ornament {
    position: absolute;
    border-radius: 45% 55% 50% 50%;
    opacity: 0.75;
  }
  .ornament--olive  { left: 84px;  top: 79px; width: 206px; height: 187px; background: radial-gradient(circle at 60% 55%, var(--olive-deep), transparent 70%); }
  .ornament--silver { left: 500px; top: 14px; width: 210px; height: 187px; background: radial-gradient(circle at 60% 55%, var(--silver-deep), transparent 70%); }
  .ornament--teal   { left: 915px; top: 75px; width: 210px; height: 182px; background: radial-gradient(circle at 60% 55%, var(--teal-deep), transparent 70%); }
  .identity {
    position: absolute;
    left: 0;
    width: 100%;
    text-align: center;
    margin: 0;
  }
  .identity__name {
    top: 238px;
    font-family: "Audiowide", sans-serif;
    font-size: 52px;
    letter-spacing: 4px;
    color: var(--paper);
    font-weight: 400;
  }
  .identity__company {
    top: 326px;
    font-family: "Audiowide", sans-serif;
    font-size: 52px;
    letter-spacing: 4px;
    color: var(--brand-blue);
  }
  .identity__role {
    top: 436px;
    font-family: "Cinzel", serif;
    font-size: 31px;
    color: var(--title-green);
  }
  .rule {
    position: absolute;
    left: 0;
    width: 100%;
    height: 6px;
    background: var(--paper);
  }
  .rule--upper { top: 530px; }
  .rule--lower { top: 640px; }
  .contact-band {
    position: absolute;
    top: 536px;
    left: 0;
    width: 100%;
    height: 104px;
    background: var(--band-blue);
    font-family: "Marcellus", serif;
    font-size: 29px;
    color: var(--paper);
  }
  .contact-band__item {
    position: absolute;
    top: 50%;
    transform: translateY(-50%);
    margin: 0;
    white-space: nowrap;
  }
  .contact-band__item--mobile { left: 98px; }
  .contact-band__item--email  { left: 654px; }
</style>
</head>
<body>
  <main class="card">
    <div class="tone-panel tone-panel--olive"></div>
    <div class="tone-panel tone-panel--silver"></div>
    <div class="tone-panel tone-panel--teal"></div>

    <div class="ornament ornament--olive" role="img" aria-label="Decorative olive heart and swirl ornament"></div>
    <div class="ornament ornament--silver" role="img" aria-label="Decorative silver heart and swirl ornament"></div>
    <div class="ornament ornament--teal" role="img" aria-label="Decorative teal heart and swirl ornament"></div>

    <h1 class="identity identity__name">GARETH WILMSLOW</h1>
    <p class="identity identity__company">MORVEK IT LIMITED</p>
    <p class="identity identity__role">IT CONSULTANT</p>

    <div class="rule rule--upper"></div>
    <section class="contact-band">
      <p class="contact-band__item contact-band__item--mobile">Mobile : 07912563084</p>
      <p class="contact-band__item contact-band__item--email">E-mail : garethwk@fernmail.co.uk</p>
    </section>
    <div class="rule rule--lower"></div>
  </main>
</body>
</html>
```